law firm website

We need a website for our law firm that is based in Kabul, Afghanistan. We provide legal and government affairs services for the international community. We would like to see designs that use the colors of our logo, designs that are elegant and simple, yet not boring or over the top. No law or law related symbols or pictures. We would like clocks that show times for Kabul, Dubai and Washington DC.
Updates
Reason: No designs that are up to the task as yet. Perhaps we should stop using picture of people, that obviously don't work with us, in the website. If you are to use pictures, please try using pictures of Afghanistan mountains, art, craft etc. Also, please make the clocks very small - they seem to be dominating the website. We do not sell clocks or watches - we are a law firm. Hope you all understand and thank you for your designs to date.
Deal All,
Industry/Entity Type
Government
Requirements
Must have
- our logo.
the following phrases/words in flash.
"international standards" "local expertise" "integrity" "clarity" "commitment" "Afghanistan"
clocks: kabul, dubai, washington dc
Should not have
- law related pictures
afghanistan flag colors

```html
<!DOCTYPE html>
<html lang="en">
<head>
<meta charset="utf-8">
<title>Hindukush Counsel Partners</title>
<link href="https://fonts.googleapis.com/css2?family=Arimo:ital,wght@0,400;0,700;1,400&display=swap" rel="stylesheet">
<style>
:root{
  --brand:#35a6d9;
  --nav:#58585a;
  --ink:#555;
  --ink-soft:#777;
  --heading:#2f9fd6;
  --rule:#d4d4d4;
  --white:#fff;
}
*{margin:0;padding:0;box-sizing:border-box}
html,body{width:1200px;height:1105px;overflow:hidden;background:var(--white);font-family:"Arimo",Arial,sans-serif;color:var(--ink)}
.page{position:relative;width:1200px;height:1105px}
.abs{position:absolute}
.top-band{left:180px;top:0;width:840px;height:6px;background:var(--brand)}
.brand{left:180px;top:47px;display:flex;align-items:center;gap:10px}
.brand-mark{width:14px;height:14px;background:var(--nav)}
.brand-name{font-size:18px;color:var(--brand)}
.social{left:628px;top:54px;display:flex;gap:7px}
.social span{width:27px;height:27px;border-radius:50%;background:#6b6e73;display:block}
.clocks{left:797px;top:19px;display:flex;gap:18px}
.clock{width:60px;text-align:center;font-size:10.5px;color:#333}
.clock svg{display:block;margin:0 auto 5px}
.clock:last-child{width:70px}
.nav{left:180px;top:109px;width:840px;height:44px;background:var(--nav);display:flex;justify-content:space-around;align-items:center;padding:0 12px}
.nav a{color:var(--white);font-size:12.5px;text-decoration:none}
.hero{left:180px;top:153px;width:840px;height:355px;background:linear-gradient(180deg,#4c7bbf 0%,#9ab6d6 28%,#8a8a80 45%,#9b9a8f 55%,#8f9a9a 66%,#4f6b39 80%,#2f4a22 100%)}
.hero-title{left:180px;top:313px;width:840px;text-align:center;font-size:29px;color:var(--white);text-shadow:0 1px 3px rgba(0,0,0,.35)}
.hero-arrows{left:947px;top:479px;display:flex;gap:2px}
.hero-arrows span{width:30px;height:17px;background:#2e3a55;display:flex;align-items:center;justify-content:center}
.services{left:180px;top:518px;width:840px;height:194px;display:flex;gap:9px}
.service{flex:1;background:var(--brand);color:var(--white);text-align:center;display:flex;flex-direction:column;align-items:center;padding-top:36px}
.service h3{font-weight:400;font-size:15px;line-height:24px;margin-top:8px}
.service p{font-size:10px;margin-top:6px}
.about{left:180px;top:740px;width:300px}
h2{font-weight:400;font-size:15px;color:var(--heading)}
.about p{font-size:10.3px;line-height:19px;margin-top:14px;color:var(--ink)}
.about p+p{margin-top:19px}
.btn{display:inline-block;margin-top:15px;width:96px;height:30px;line-height:30px;text-align:center;background:#4b4b4d;color:var(--white);font-size:12px;border-radius:2px}
.testi-head{left:510px;top:740px}
.testi-nav{left:997px;top:745px;font-size:11px;color:#aaa;letter-spacing:6px}
.testi{top:770px;width:205px}
.quote-open,.quote-close{position:absolute;font-size:34px;color:#bbb;font-family:Georgia,serif;line-height:1}
.quote-open{left:-20px;top:-2px}
.quote-close{right:0;top:120px}
.testi p{font-size:10.3px;line-height:19px;padding-top:12px;color:var(--ink)}
.testi .who{margin-top:20px;font-size:11.5px;color:var(--heading)}
.testi .date{margin-top:7px;font-size:9.5px;font-style:italic;color:var(--ink-soft)}
.divider{left:765px;top:778px;width:1px;height:160px;background:var(--rule)}
.footer-rule{left:180px;top:994px;width:840px;height:5px;background:var(--rule)}
.footer-nav{left:185px;top:1024px;font-size:9.5px;color:#444}
.footer-nav span{margin:0 7px}
.copy{left:185px;top:1047px;font-size:9.5px;color:#444}
.partner{left:900px;top:1028px;font-size:20px;color:#444}
</style>
</head>
<body>
<div class="page">
  <div class="abs top-band"></div>

  <div class="abs brand">
    <span class="brand-mark"></span>
    <span class="brand-name">Hindukush Counsel Partners</span>
  </div>

  <div class="abs social" aria-label="Social links"><span></span><span></span><span></span><span></span></div>

  <div class="abs clocks">
    <div class="clock">
      <svg width="60" height="60" viewBox="0 0 60 60"><rect x="1" y="1" width="58" height="58" rx="3" fill="#e6e6e6" stroke="#bbb"/><circle cx="30" cy="30" r="24" fill="#f7f7f7"/><g fill="#222"><circle cx="30" cy="10" r="1.3"/><circle cx="30" cy="50" r="1.3"/><circle cx="10" cy="30" r="1.3"/><circle cx="50" cy="30" r="1.3"/><circle cx="40" cy="12.7" r="1"/><circle cx="47.3" cy="20" r="1"/><circle cx="47.3" cy="40" r="1"/><circle cx="40" cy="47.3" r="1"/><circle cx="20" cy="47.3" r="1"/><circle cx="12.7" cy="40" r="1"/><circle cx="12.7" cy="20" r="1"/><circle cx="20" cy="12.7" r="1"/></g><path d="M30 30 L20 22 M30 30 L42 19" stroke="#111" stroke-width="2.5" stroke-linecap="round"/><path d="M30 30 L40 42" stroke="#d22" stroke-width="1"/></svg>kabul
    </div>
    <div class="clock">
      <svg width="60" height="60" viewBox="0 0 60 60"><rect x="1" y="1" width="58" height="58" rx="3" fill="#e6e6e6" stroke="#bbb"/><circle cx="30" cy="30" r="24" fill="#f7f7f7"/><g fill="#222"><circle cx="30" cy="10" r="1.3"/><circle cx="30" cy="50" r="1.3"/><circle cx="10" cy="30" r="1.3"/><circle cx="50" cy="30" r="1.3"/><circle cx="40" cy="12.7" r="1"/><circle cx="47.3" cy="20" r="1"/><circle cx="47.3" cy="40" r="1"/><circle cx="40" cy="47.3" r="1"/><circle cx="20" cy="47.3" r="1"/><circle cx="12.7" cy="40" r="1"/><circle cx="12.7" cy="20" r="1"/><circle cx="20" cy="12.7" r="1"/></g><path d="M30 30 L20 22 M30 30 L42 19" stroke="#111" stroke-width="2.5" stroke-linecap="round"/><path d="M30 30 L40 42" stroke="#d22" stroke-width="1"/></svg>Dubai
    </div>
    <div class="clock">
      <svg width="60" height="60" viewBox="0 0 60 60"><rect x="1" y="1" width="58" height="58" rx="3" fill="#e6e6e6" stroke="#bbb"/><circle cx="30" cy="30" r="24" fill="#f7f7f7"/><g fill="#222"><circle cx="30" cy="10" r="1.3"/><circle cx="30" cy="50" r="1.3"/><circle cx="10" cy="30" r="1.3"/><circle cx="50" cy="30" r="1.3"/><circle cx="40" cy="12.7" r="1"/><circle cx="47.3" cy="20" r="1"/><circle cx="47.3" cy="40" r="1"/><circle cx="40" cy="47.3" r="1"/><circle cx="20" cy="47.3" r="1"/><circle cx="12.7" cy="40" r="1"/><circle cx="12.7" cy="20" r="1"/><circle cx="20" cy="12.7" r="1"/></g><path d="M30 30 L20 22 M30 30 L42 19" stroke="#111" stroke-width="2.5" stroke-linecap="round"/><path d="M30 30 L40 42" stroke="#d22" stroke-width="1"/></svg>washington dc
    </div>
  </div>

  <nav class="abs nav">
    <a href="#">Home</a><a href="#">About Us</a><a href="#">People</a><a href="#">Services</a><a href="#">Ethics</a><a href="#">Publications</a><a href="#">LexOrbit</a><a href="#">Contact us</a>
  </nav>

  <div class="abs hero" role="img" aria-label="Panorama of Afghan mountains above a wide river valley under a blue sky"></div>
  <div class="abs hero-title">Integrity - clarity - commitment</div>
  <div class="abs hero-arrows">
    <span><svg width="16" height="6" viewBox="0 0 16 6"><path d="M15 3H2M4 1L1.5 3 4 5" stroke="#fff" fill="none" stroke-width="1"/></svg></span>
    <span><svg width="16" height="6" viewBox="0 0 16 6"><path d="M1 3h13M12 1l2.5 2L12 5" stroke="#fff" fill="none" stroke-width="1"/></svg></span>
  </div>

  <section class="abs services">
    <div class="service">
      <div role="img" aria-label="Icon of two business partners seated" style="width:76px;height:58px;background:rgba(255,255,255,.25)"></div>
      <h3>Corporate and<br>investment</h3>
      <p>[ Click here for view more details ]</p>
    </div>
    <div class="service">
      <svg width="44" height="60" viewBox="0 0 44 60"><rect x="1" y="1" width="42" height="58" rx="5" fill="#fff"/><rect x="6" y="6" width="32" height="10" rx="1" fill="#35a6d9"/><g fill="#35a6d9"><circle cx="11" cy="25" r="4"/><circle cx="22" cy="25" r="4"/><circle cx="33" cy="25" r="4"/><circle cx="11" cy="36" r="4"/><circle cx="22" cy="36" r="4"/><circle cx="33" cy="36" r="4"/><circle cx="11" cy="47" r="4"/><circle cx="22" cy="47" r="4"/><circle cx="33" cy="47" r="4"/></g></svg>
      <h3 style="margin-top:12px">Tax</h3>
      <p>[ Click here for view more details ]</p>
    </div>
    <div class="service">
      <svg width="52" height="54" viewBox="0 0 52 54"><path d="M1 0V53H52" stroke="#fff" stroke-dasharray="2 2" fill="none"/><rect x="5" y="5" width="14" height="47" fill="#fff"/><rect x="21" y="23" width="14" height="29" fill="#fff"/><rect x="37" y="36" width="14" height="16" fill="#fff"/></svg>
      <h3>Financings</h3>
      <p>[ Click here for view more details ]</p>
    </div>
    <div class="service">
      <svg width="54" height="54" viewBox="0 0 54 54"><path d="M3 52 L20 30 L28 40 L44 16" stroke="#fff" stroke-width="5" fill="none"/><path d="M36 10 L53 1 L51 21 Z" fill="#fff"/></svg>
      <h3>Dispute resolution</h3>
      <p>[ Click here for view more details ]</p>
    </div>
  </section>

  <section class="abs about">
    <h2>About Hindukush Counsel Partners</h2>
    <p>We are an Afghan legal and government relations advisory firm staffed by experienced lawyers from Afghanistan, the United States and Australia.</p>
    <p>We provide premium legal, regulatory, tax and government relations advisory services to development finance institutions, businesses, investors, non-government organizations and government agencies.</p>
    <span class="btn">Read More</span>
  </section>

  <h2 class="abs testi-head">Client Testimonials</h2>
  <div class="abs testi-nav">‹›</div>

  <article class="abs testi" style="left:530px">
    <span class="quote-open">“</span>
    <p>Prof. Rahimi is an Afghan-American advocate registered with the Afghanistan Independent Bar Association.&nbsp; He has worked extensively in Afghanistan in the legal and government affairs environments over several years including...</p>
    <span class="quote-close">”</span>
    <div class="who">Karim Nadeem Rahimi</div>
    <div class="date">Posted on 27 Nov 2013</div>
  </article>
  <div class="abs divider"></div>
  <article class="abs testi" style="left:811px">
    <span class="quote-open">“</span>
    <p>Prof. Rahimi is an Afghan-American advocate registered with the Afghanistan Independent Bar Association.&nbsp; He has worked extensively in Afghanistan in the legal and government affairs environments over several years including...</p>
    <span class="quote-close">”</span>
    <div class="who">Karim Nadeem Rahimi</div>
    <div class="date">Posted on 27 Nov 2013</div>
  </article>

  <div class="abs footer-rule"></div>
  <div class="abs footer-nav">Home<span>|</span>About Us<span>|</span>People<span>|</span>Services<span>|</span>Ethics<span>|</span>Publications<span>|</span>LexOrbit<span>|</span>Contact us</div>
  <div class="abs copy">Copyrights © 2013 Hindukush Counsel Partners. All Rights Reserved.</div>

  <div class="abs partner">LexOrbit</div>
</div>
</body>
</html>
```